Cedar Hollow responsive web design

We need a responsive, bootstrap compatible (but design only - PSD files) website design for a fly fishing shop and guide service.

Design should be very clean. Home Page design + interior page design please.

Possible Home Page Content:
Slide Show
Highlight Three Features: Guided Trips, Fly Shop, Missouri River
About

Thank you and good luck!

Shop

• This will be used on Bootstrap CMS so needs 12 column bootstrap measurements.

DESIGN ONLY NEEDED (clean PSD files), no programming required.
Need a Home Page layout and secondary page layout

Must show use of the following:
H1 - H5 font uses
link color
Dropdown for navigation bar
Button example
• No cutout images, this will be part of CMS and client needs to be able to update most content without knowing photoshop.

```html
<!DOCTYPE html>
<html lang="en">
<head>
<meta charset="utf-8">
<title>Cedar Hollow – Blog</title>
<link rel="stylesheet" href="https://fonts.googleapis.com/css2?family=Oswald:wght@400;500&family=Source+Sans+3:wght@400;600&display=swap">
<style>
:root{
  --header:#22090f;
  --footer-bottom:#1c1417;
  --band:#f4f4f4;
  --blue:#2a8cc6;
  --link:#1797d4;
  --red:#c7323b;
  --text:#555;
  --dark:#1b1b1b;
  --line:#dcdcdc;
}
*{box-sizing:border-box;margin:0;padding:0}
html,body{width:1027px;height:1200px;overflow:hidden;background:#fff}
body{font-family:"Source Sans 3",sans-serif;color:var(--text);position:relative}
.abs{position:absolute}
.site-header{left:0;top:0;width:1027px;height:69px;background:var(--header)}
.header-rule{left:0;top:69px;width:1027px;height:4px;background:#d6d6d6}
.logo-box{left:129px;top:0;width:156px;height:101px;background:var(--header);border:0 solid #c9c9c9;border-width:0 5px 5px 5px;display:flex;align-items:center;justify-content:center;gap:6px}
.logo-box .mark{width:12px;height:12px;background:#5cc3ea}
.logo-box span{font-family:"Oswald",sans-serif;font-size:20px;color:#5cc3ea;font-weight:500}
.main-nav{left:390px;top:29px;display:flex;gap:0;font-family:"Oswald",sans-serif;font-size:15px;color:#fff}
.main-nav a{color:#fff;text-decoration:none}
.main-nav .sep{margin:0 16px}
.page-band{left:0;top:73px;width:1027px;height:114px;background:var(--band)}
.page-title{left:134px;top:140px;font-family:"Oswald",sans-serif;font-weight:400;font-size:26px;color:var(--blue)}
.breadcrumb{right:135px;top:155px;font-size:13px;color:#666}
.post-image-frame{left:133px;top:226px;width:486px;height:169px;border:1px solid var(--line);padding:7px}
.post-image{width:100%;height:100%;background:linear-gradient(135deg,#5b5a2c,#8a7f4a 45%,#d9d2bd 70%,#6e6434)}
.post-title{left:134px;top:405px;font-family:"Oswald",sans-serif;font-weight:400;font-size:18px;color:var(--dark)}
.post-meta{left:134px;top:437px;font-size:11px;color:#333;display:flex;gap:12px;align-items:center}
.post-meta svg{vertical-align:-1px;margin-right:4px}
.post-body{left:134px;top:467px;width:486px;font-size:13.5px;line-height:16px;color:#666}
.comment-label{left:134px;top:547px;font-size:12.5px;color:var(--link)}
.comment-box{left:133px;top:577px;width:487px;height:175px;border:1px solid var(--line);background:#fff}
.btn-submit{left:133px;top:783px;width:181px;height:36px;background:var(--red);color:#fff;font-family:"Oswald",sans-serif;font-size:17px;display:flex;align-items:center;justify-content:center}
.sidebar{left:645px;top:187px;width:382px;height:669px;background:linear-gradient(90deg,#f1f1f1,#fff 30px)}
.sidebar-title{left:670px;top:222px;font-family:"Oswald",sans-serif;font-weight:400;font-size:17px;color:var(--dark)}
.report{left:670px;width:225px}
.report h4{font-size:12.5px;font-weight:600;color:var(--link);letter-spacing:.2px}
.report p{font-size:10.5px;line-height:13.5px;color:#666;margin-top:7px;padding-left:1px}
.report .btn{display:inline-flex;align-items:center;justify-content:center;width:77px;height:26px;border:1px solid #222;font-family:"Oswald",sans-serif;font-size:12px;color:#222;margin:12px 0 0 3px}
.report .btn.active{background:var(--red);border-color:var(--red);color:#fff}
.report .dots{border-bottom:2px dotted #888;margin:14px 0 0 5px;width:220px}
.site-footer{left:0;top:856px;width:1027px;height:294px;background:linear-gradient(160deg,#3a332c,#2b2523 50%,#3b3430)}
.footer-heading{font-family:"Oswald",sans-serif;font-weight:400;font-size:20px;color:#3fa6dc}
.view-all{left:335px;top:895px;font-family:"Oswald",sans-serif;font-size:12px;color:#fff;text-decoration:underline}
.gallery{left:133px;top:946px;display:grid;grid-template-columns:repeat(3,78px);grid-gap:6px}
.thumb{height:77px;border:1px solid #ddd;padding:4px}
.thumb div{width:100%;height:100%}
.social{left:411px;top:945px}
.social li{list-style:none;display:flex;align-items:center;height:36px;margin-bottom:5px;font-size:12.5px;font-weight:600;letter-spacing:.6px;color:#fff}
.social .sq{width:36px;height:36px;margin-right:11px}
.contact-text{left:654px;top:944px;width:240px;font-size:11.5px;line-height:16px;color:#fff;font-weight:600}
.contact-line{left:654px;display:flex;gap:10px;font-size:11.5px;line-height:19px;color:#fff}
.contact-line svg{flex:none;margin-top:2px}
.copyright{left:0;top:1150px;width:1027px;height:50px;background:var(--footer-bottom);display:flex;align-items:center;justify-content:center;font-size:12px;color:#999}
.copyright strong{color:#fff;font-weight:400;margin-left:4px}
</style>
</head>
<body>
<header class="abs site-header"></header>
<div class="abs header-rule"></div>
<div class="abs logo-box"><i class="mark"></i><span>Cedar Hollow</span></div>
<nav class="abs main-nav">
  <a href="#">Home</a><span class="sep">/</span><a href="#">About Us</a><span class="sep">/</span><a href="#">Guided Trips</a><span class="sep">/</span><a href="#">Fly Shop</a><span class="sep">/</span><a href="#">Missouri River</a><span class="sep">/</span><a href="#">Contact Us</a>
</nav>

<div class="abs page-band"></div>
<h1 class="abs page-title">Our Recent Blog</h1>
<div class="abs breadcrumb">You are here:Home / Blog</div>

<div class="abs post-image-frame"><div class="post-image" role="img" aria-label="Young angler in a cap sitting in a drift boat on the river"></div></div>
<h2 class="abs post-title">Post Standard One</h2>
<div class="abs post-meta">
  <span><svg width="9" height="9" viewBox="0 0 9 9"><rect x=".5" y="1.5" width="8" height="7" fill="none" stroke="#333"/><rect x=".5" y="1.5" width="8" height="2" fill="#333"/></svg>January 26, 2014</span>
  <span><svg width="8" height="9" viewBox="0 0 8 9"><circle cx="4" cy="2.5" r="2" fill="#333"/><path d="M0 9c0-3 2-4 4-4s4 1 4 4z" fill="#333"/></svg>Marcus Hale</span>
  <span><svg width="10" height="9" viewBox="0 0 10 9"><ellipse cx="5" cy="4" rx="5" ry="3.5" fill="#333"/></svg>3 Comments</span>
</div>
<p class="abs post-body">Duis et ultrices nibh. Donec et eros ac eros aliquam vestibulum eget id lectus. Duis sed congue tortor, in molestie sem. Nulla nec ultricies ipsum. Aenean suscipit, nulla ut blandit semper, odio odio interdum velit, sed iaculis sapien lorem non erat. Donec eu justo nibh. Sed consequat ante tincidunt aliquam tristique.</p>
<a class="abs comment-label">Leave a comment*</a>
<div class="abs comment-box"></div>
<div class="abs btn-submit">Submit Now</div>

<aside class="abs sidebar"></aside>
<h3 class="abs sidebar-title">FISHING REPORTS</h3>
<div class="abs report" style="top:262px"><h4>MADISON RIVER - UPPER</h4><p>October 10th, 2013<br>Temperature: 52 ° F<br>Fishing: Good</p><span class="btn active">Read More</span><div class="dots"></div></div>
<div class="abs report" style="top:390px"><h4>MADISON RIVER - UPPER</h4><p>October 10th, 2013<br>Temperature: 52 ° F<br>Fishing: Good</p><span class="btn">Read More</span><div class="dots"></div></div>
<div class="abs report" style="top:523px"><h4>MADISON RIVER - UPPER</h4><p>October 10th, 2013<br>Temperature: 52 ° F<br>Fishing: Good</p><span class="btn">Read More</span><div class="dots"></div></div>
<div class="abs report" style="top:655px"><h4>MADISON RIVER - UPPER</h4><p>October 10th, 2013<br>Temperature: 52 ° F<br>Fishing: Good</p><span class="btn">Read More</span><div class="dots"></div></div>

<footer class="abs site-footer" role="img" aria-label="Dim interior of the fly shop behind the footer"></footer>
<h3 class="abs footer-heading" style="left:133px;top:884px">OUR GALLERY</h3>
<a class="abs view-all">View All</a>
<div class="abs gallery">
  <div class="thumb"><div role="img" aria-label="Shop building exterior" style="background:linear-gradient(#8aa6c8,#a0a39a)"></div></div>
  <div class="thumb"><div role="img" aria-label="Shop interior" style="background:linear-gradient(#6b5a3e,#2e2a26)"></div></div>
  <div class="thumb"><div role="img" aria-label="Shop interior" style="background:linear-gradient(#6b5a3e,#2e2a26)"></div></div>
  <div class="thumb"><div role="img" aria-label="Anglers on the river" style="background:linear-gradient(#8a8a7a,#4f5a55)"></div></div>
  <div class="thumb"><div role="img" aria-label="River canyon" style="background:linear-gradient(#9aaec4,#7a4a3a 50%,#3c4a48)"></div></div>
  <div class="thumb"><div role="img" aria-label="River canyon" style="background:linear-gradient(#9aaec4,#7a4a3a 50%,#3c4a48)"></div></div>
</div>

<h3 class="abs footer-heading" style="left:410px;top:884px">CONNECT WITH US</h3>
<ul class="abs social">
  <li><span class="sq" style="background:#2b4a8a"></span>FRIENDSPACE</li>
  <li><span class="sq" style="background:#49b3e0"></span>CHIRPER</li>
  <li><span class="sq" style="background:#f08a1c"></span>BLOG</li>
  <li><span class="sq" style="background:#1b8fd0"></span>WORKLINK</li>
</ul>

<h3 class="abs footer-heading" style="left:654px;top:884px">CONTECT US</h3>
<p class="abs contact-text">Lorem ipsum dolor sit amet, consectetur elit. Suspendisse quis tincidunt odio. Nullam nec semper nisi orci suscipit gravida.</p>
<div class="abs contact-line" style="top:1010px"><svg width="19" height="16" viewBox="0 0 19 16"><path d="M9.5 0L0 8h3v8h5v-5h3v5h5V8h3z" fill="#fff"/></svg><span style="margin-left:0">418 Willow Creek Road<br>Bozeman, MT 59715</span></div>
<div class="abs contact-line" style="top:1059px"><svg width="19" height="13" viewBox="0 0 19 13"><path d="M1 4c4-4 13-4 17 0l-3 2-2-2H6L4 6z" fill="#fff"/><rect x="4" y="6" width="11" height="7" fill="#fff"/></svg><span>(406) 555-0182</span></div>
<div class="abs contact-line" style="top:1089px"><svg width="19" height="12" viewBox="0 0 19 12"><rect x=".5" y=".5" width="18" height="11" fill="none" stroke="#fff"/><path d="M.5.5l9 6 9-6" fill="none" stroke="#fff"/></svg><span>info@cedarhollow.com</span></div>

<div class="abs copyright">Copyright © 2014 <strong>Cedar Hollow.</strong></div>
</body>
</html>
```